Restaurant Bar website in Oakland

Landing page that looks good on mobile and home. Easy to make changes to SEO and Menu page .
Might link with online ordering through the point of sale provider or not. Either way we want to be able to upload menus.
No forms need. Just landing page, about page with a paragraph and a few photos, address, hours and a mailto info@
A press page and an faq

Target Market(s)

Customers

Coding

Coded - Design and coding required

Number of Pages Required

4 page

Colors
00a990
ffc214

Requirements
Must have
• Simple to scroll
SEO
Simple to add menus
Our logo

```html
<!DOCTYPE html>
<html lang="en">
<head>
<meta charset="utf-8">
<title>Marlow's — Restaurant &amp; Bar</title>
<link href="https://fonts.googleapis.com/css2?family=Cinzel:wght@600;700&family=Montserrat:wght@400;500;600;700&family=Lato:wght@400;700&display=swap" rel="stylesheet">
<style>
:root{
  --teal:#00a990;
  --teal-dark:#007a68;
  --yellow:#ffc214;
  --yellow-soft:#ffd04d;
  --ink:#222222;
  --text:#555555;
  --muted:#f4f4f4;
  --line:#dddddd;
  --white:#ffffff;
}
*{box-sizing:border-box;margin:0;padding:0}
html,body{width:1200px;height:3831px;overflow:hidden}
body{position:relative;background:var(--white);font-family:'Lato',sans-serif;color:var(--text)}
.abs{position:absolute}
.display{font-family:'Cinzel',serif;font-weight:700;color:var(--ink)}

/* header */
.site-header{left:0;top:0;width:1200px;height:112px;background:var(--yellow)}
.brand-panel{left:0;top:0;width:290px;height:112px}
.brand-name{left:76px;top:36px;font-family:'Montserrat',sans-serif;font-weight:700;font-size:30px;letter-spacing:3px;color:var(--yellow)}
.main-nav{left:462px;top:42px;display:flex;font-family:'Montserrat',sans-serif;font-size:14px}
.main-nav a{color:var(--ink);text-decoration:none;display:block;height:30px;line-height:30px;padding:0 26px}
.main-nav a.active{background:var(--teal-dark);color:var(--white);border-radius:15px}
.header-icons{left:975px;top:46px;display:flex;gap:22px}

/* hero */
.hero{left:0;top:112px;width:1200px;height:669px;background:linear-gradient(160deg,#5e6660 0%,#6f5a40 40%,#a7743e 70%,#4f3a24 100%)}
.hero-title{left:0;top:405px;width:1200px;text-align:center;font-size:43px;color:var(--white);letter-spacing:1px}
.hero-sub{left:0;top:458px;width:1200px;text-align:center;font-size:15px;line-height:20px;color:var(--white)}
.hero-btn{left:500px;top:521px;width:206px;height:46px;border-radius:23px;background:var(--yellow);color:var(--ink);font-family:'Montserrat',sans-serif;font-size:13px;line-height:46px;padding-left:40px}
.hero-btn-mark{left:650px;top:521px;width:56px;height:46px;border-radius:0 23px 23px 0;background:var(--teal-dark)}
.hero-btn-mark span{position:absolute;left:16px;top:12px;width:22px;height:22px;border:2px solid var(--yellow);border-radius:50%}
.slider-dots{left:30px;top:392px}
.slider-dots i{display:block;width:5px;height:5px;border-radius:50%;background:#c9c9c9;margin-bottom:10px}

/* booking */
.booking{left:113px;top:714px;width:975px;height:143px;background:var(--yellow)}
.field{position:absolute;top:45px;height:50px;background:var(--white);font-size:12px;color:var(--ink);line-height:50px;padding-left:15px}
.field .ico{position:absolute;right:0;top:0;width:48px;height:50px;border-left:1px solid var(--line);display:flex;align-items:center;justify-content:center}
.field-label{position:absolute;top:45px;line-height:50px;font-size:12px;color:var(--ink)}
.book-btn{position:absolute;left:723px;top:45px;width:207px;height:50px;border-radius:25px;background:var(--teal-dark);color:var(--white);font-family:'Montserrat',sans-serif;font-weight:700;font-size:12px;text-align:center;line-height:50px}

/* features */
.features{left:0;top:857px;width:1200px;height:209px;background:var(--muted)}
.feature{position:absolute;top:60px}
.feature h3{font-family:'Montserrat',sans-serif;font-weight:600;font-size:19px;color:var(--teal-dark);letter-spacing:.5px}
.feature p{font-size:14px;line-height:19px;color:var(--text);margin-top:4px}
.feature-divider{position:absolute;top:50px;width:1px;height:90px;background:#d8d8d8}

/* about */
.section-title{width:1200px;left:0;text-align:center;font-size:31px}
.about-corner{left:104px;top:1218px;width:132px;height:136px;border-top:6px solid var(--yellow);border-left:6px solid var(--yellow)}
.about-photo{left:113px;top:1227px;width:452px;height:376px;background:linear-gradient(135deg,#3e5850 0%,#8d6b52 45%,#b88760 70%,#5d4a3f 100%)}
.about-badge{left:479px;top:1303px;width:120px;height:114px;background:var(--teal-dark);display:flex;align-items:center;justify-content:center}
.about-badge span{width:54px;height:54px;border:2px solid var(--yellow);border-radius:50%}
.about-rule{left:584px;top:1260px;width:60px;height:4px;background:var(--teal-dark)}
.about-heading{left:660px;top:1242px;font-family:'Montserrat',sans-serif;font-weight:400;font-size:30px;color:var(--ink)}
.about-copy{left:644px;top:1298px;width:448px;font-size:12.5px;line-height:22.5px;color:var(--text)}
.about-copy p{margin-bottom:22px}
.pill{background:var(--yellow);color:var(--ink);font-family:'Montserrat',sans-serif;font-size:13px;text-align:center;border-radius:23px}
.about-btn{left:644px;top:1558px;width:184px;height:46px;line-height:46px}

/* menu */
.menu-section{left:0;top:1716px;width:1200px;height:727px;background:linear-gradient(180deg,#2a2520 0%,#3a3128 40%,#2e2923 75%,#221e1a 100%)}
.menu-title{top:1775px;color:var(--white)}
.menu-tabs{left:0;top:1830px;width:1200px;display:flex;justify-content:center;gap:50px;font-family:'Montserrat',sans-serif;font-size:18px;color:var(--white)}
.menu-tabs span.active{color:var(--yellow);border-bottom:2px solid var(--yellow);padding-bottom:6px}
.dish{position:absolute;width:481px;height:134px;background:var(--white)}
.dish-photo{position:absolute;left:12px;top:10px;width:121px;height:114px}
.dish-photo.ribs{background:linear-gradient(135deg,#5a7a3a,#8a3a2a 45%,#c25a3a 70%,#eae2d8)}
.dish-photo.fried{background:linear-gradient(135deg,#e8dcc8,#c58a3e 45%,#9a5a22 75%,#f2ebe0)}
.dish-photo.skewer{background:linear-gradient(135deg,#c8362a,#d85a3a 40%,#5a8a3a 65%,#e8e0d4)}
.dish h4{position:absolute;left:153px;top:20px;width:318px;white-space:nowrap;font-family:'Montserrat',sans-serif;font-weight:600;font-size:16px;color:var(--ink)}
.dish h4::after{content:"";position:absolute;left:0;top:25px;width:48px;border-bottom:2px dashed var(--ink)}
.dish p{position:absolute;left:154px;top:52px;width:300px;font-size:12.5px;line-height:15px;color:var(--text)}
.dish .price{position:absolute;left:153px;top:97px;font-size:17px;color:#d9a100}

/* faq */
.faq-title{left:110px;top:2532px;font-size:29px}
.faq-title-rule{left:110px;top:2578px;width:220px;height:2px;background:var(--ink)}
.faq-item{position:absolute;left:112px;width:468px;border:1px solid var(--line);font-family:'Montserrat',sans-serif;font-size:14px;color:var(--ink);padding:0 16px;letter-spacing:.3px}
.faq-item.short{height:36px;line-height:34px}
.faq-item .dot{position:absolute;right:10px;top:10px;width:15px;height:15px;border-radius:50%;background:var(--teal-dark)}
.faq-item .dot::after{content:"";position:absolute;left:5px;top:4px;width:4px;height:4px;border-left:1.5px solid #fff;border-bottom:1.5px solid #fff;transform:rotate(45deg)}
.faq-item.open{height:96px;padding-top:12px}
.faq-item.open .dot{top:14px}
.faq-item.open .dot::after{transform:rotate(-45deg);top:3px}
.faq-item.open p{font-family:'Lato',sans-serif;font-size:12.5px;line-height:15px;color:var(--text);margin-top:8px;letter-spacing:0}

.hours{left:633px;top:2540px;width:454px;height:437px;background:linear-gradient(160deg,#ffc214 0%,#e8ad0a 50%,#ffc93a 100%)}
.hours-frame{position:absolute;left:18px;top:22px;width:418px;height:395px;border:2px solid rgba(255,255,255,.8)}
.hours-kicker{position:absolute;left:0;top:72px;width:454px;text-align:center;font-family:'Montserrat',sans-serif;font-size:13px;color:var(--ink);letter-spacing:1px}
.hours-title{position:absolute;left:0;top:92px;width:454px;text-align:center;font-size:30px;color:var(--teal-dark)}
.hours-row{position:absolute;left:112px;font-family:'Montserrat',sans-serif;font-size:14px;color:var(--ink);display:flex;align-items:center;gap:8px}
.hours-btn{position:absolute;left:143px;top:236px;width:162px;height:48px;background:var(--teal-dark);color:var(--white);font-family:'Montserrat',sans-serif;font-size:13px;text-align:center;line-height:48px}
.contact-chip{position:absolute;top:326px;display:flex;align-items:center;gap:8px;font-family:'Montserrat',sans-serif;color:var(--ink)}
.contact-chip .circle{width:50px;height:50px;border-radius:50%;background:var(--teal-dark);display:flex;align-items:center;justify-content:center}
.contact-chip b{display:block;font-size:13px;font-weight:600}
.contact-chip span.t{font-size:13px}

/* follow */
.follow-title{top:3062px;font-size:30px}
.follow-sub{left:0;top:3104px;width:1200px;text-align:center;font-family:'Montserrat',sans-serif;font-size:13px;color:var(--ink);letter-spacing:1px}
.insta{position:absolute;top:3148px;width:195px;height:195px}

/* footer */
.site-footer{left:0;top:3398px;width:1200px;height:358px;background:var(--teal-dark)}
.footer-brand{left:76px;top:140px;font-family:'Montserrat',sans-serif;font-weight:700;font-size:36px;letter-spacing:3px;color:var(--yellow)}
.footer-col{position:absolute;top:90px;color:var(--white)}
.footer-col h5{font-family:'Cinzel',serif;font-weight:600;font-size:13px;letter-spacing:.5px;padding-bottom:6px;border-bottom:1px solid var(--yellow);display:inline-block}
.footer-col ul{list-style:none;margin-top:26px;font-size:13px}
.footer-col li{margin-bottom:11px}
.footer-col li::before{content:"> "}
.footer-col li.active{color:var(--yellow)}
.contact-line{display:flex;gap:12px;font-size:13px;line-height:20px;margin-bottom:6px}
.newsletter p{font-size:12.5px;line-height:15px;margin-top:22px;width:270px}
.news-input{width:266px;height:40px;border-radius:20px;background:var(--white);margin-top:12px;font-size:12px;color:#aaa;font-style:italic;line-height:40px;padding-left:18px}
.news-btn{width:266px;height:40px;line-height:40px;margin-top:8px;border-radius:20px}
.copyright{left:76px;top:3786px;font-size:12px;color:var(--ink)}
.socials{left:947px;top:3776px;display:flex;gap:13px}
.socials span{width:34px;height:34px;border-radius:50%;background:var(--teal-dark)}
</style>
</head>
<body>

<header class="abs site-header">
  <svg class="abs brand-panel" viewBox="0 0 290 112" aria-hidden="true"><polygon points="0,0 290,0 232,112 0,112" fill="#007a68"/></svg>
  <div class="abs brand-name">MARLOW'S</div>
  <nav class="abs main-nav">
    <a class="active" href="#">Home</a><a href="#">About us</a><a href="#">Menu</a><a href="#">FAQs</a><a href="#">Contact us</a>
  </nav>
  <div class="abs header-icons">
    <svg width="20" height="20" viewBox="0 0 20 20" fill="none" stroke="#222" stroke-width="2"><circle cx="8" cy="8" r="6"/><line x1="12.5" y1="12.5" x2="18" y2="18"/></svg>
    <svg width="20" height="20" viewBox="0 0 20 20" fill="none" stroke="#222" stroke-width="1.8"><circle cx="10" cy="6" r="4"/><path d="M3 19c0-4 3-7 7-7s7 3 7 7"/></svg>
    <svg width="20" height="20" viewBox="0 0 20 20" fill="none" stroke="#222" stroke-width="1.8"><path d="M10 17S2 12 2 7a4 4 0 0 1 8-1 4 4 0 0 1 8 1c0 5-8 10-8 10z"/></svg>
    <svg width="22" height="20" viewBox="0 0 22 20" fill="none" stroke="#222" stroke-width="1.8"><path d="M1 2h3l3 11h10l2-8H6"/><circle cx="8" cy="17" r="1.5"/><circle cx="16" cy="17" r="1.5"/><circle cx="19" cy="3" r="3" fill="#007a68" stroke="none"/></svg>
  </div>
</header>

<section class="abs hero" role="img" aria-label="Friends sharing drinks and dishes around a restaurant table"></section>
<div class="abs slider-dots"><i></i><i style="background:var(--yellow)"></i><i></i></div>
<h1 class="abs display hero-title">WELCOME TO MARLOW'S</h1>
<p class="abs hero-sub">Lorem Ipsum is simply dummy ever text printing and typesetting<br>a ever since the 1500s</p>
<div class="abs hero-btn">READ MORE</div>
<div class="abs hero-btn-mark"><span></span></div>

<section class="abs booking">
  <div class="field" style="left:45px;width:195px">1 Person<span class="ico"><svg width="16" height="16" viewBox="0 0 20 20" fill="none" stroke="#555" stroke-width="1.6"><circle cx="10" cy="6" r="4"/><path d="M3 19c0-4 3-7 7-7s7 3 7 7"/></svg></span></div>
  <span class="field-label" style="left:248px">For</span>
  <div class="field" style="left:276px;width:195px">05/11/2021<span class="ico"><svg width="18" height="18" viewBox="0 0 18 18" fill="none" stroke="#555" stroke-width="1.4"><rect x="2" y="3" width="14" height="13"/><line x1="2" y1="7" x2="16" y2="7"/><line x1="5" y1="1" x2="5" y2="4"/><line x1="13" y1="1" x2="13" y2="4"/></svg></span></div>
  <span class="field-label" style="left:481px">At</span>
  <div class="field" style="left:507px;width:195px">8:00 Pm<span class="ico"><svg width="18" height="18" viewBox="0 0 18 18" fill="none" stroke="#555" stroke-width="1.4"><circle cx="9" cy="9" r="7.5"/><path d="M9 4v5l3 2"/></svg></span></div>
  <div class="book-btn">BOOK A TABLE</div>
</section>

<section class="abs features">
  <div class="feature" style="left:112px">
    <svg class="abs" style="left:0;top:2px" width="40" height="50" viewBox="0 0 40 50" fill="none" stroke="#007a68" stroke-width="2"><path d="M4 16h32l-3 32H7z"/><path d="M12 16c0-6 4-12 8-12s8 6 8 12"/><line x1="12" y1="28" x2="28" y2="28"/></svg>
    <div style="margin-left:52px"><h3>Fresh Food</h3><p>Lorem Ipsum is simply dummy<br>a ever since the 1500s</p></div>
  </div>
  <div class="feature-divider" style="left:440px"></div>
  <div class="feature" style="left:490px">
    <svg class="abs" style="left:0;top:2px" width="30" height="52" viewBox="0 0 30 52" fill="none" stroke="#007a68" stroke-width="2"><path d="M4 2h22c2 14-2 24-11 24S2 16 4 2z"/><line x1="15" y1="26" x2="15" y2="46"/><line x1="6" y1="48" x2="24" y2="48"/></svg>
    <div style="margin-left:43px"><h3>GooD Wine</h3><p>Lorem Ipsum is simply dummy<br>a ever since the 1500s</p></div>
  </div>
  <div class="feature-divider" style="left:796px"></div>
  <div class="feature" style="left:846px">
    <svg class="abs" style="left:0;top:2px" width="40" height="54" viewBox="0 0 40 54" fill="none" stroke="#007a68" stroke-width="2"><path d="M10 16a7 7 0 0 1 4-13 8 8 0 0 1 12 0 7 7 0 0 1 4 13v6H10z"/><circle cx="20" cy="30" r="7"/><path d="M4 52c0-9 7-14 16-14s16 5 16 14"/></svg>
    <div style="margin-left:41px"><h3>Chef's Specials</h3><p>Lorem Ipsum is simply dummy<br>a ever since the 1500s</p></div>
  </div>
</section>

<h2 class="abs display section-title" style="top:1140px">ABOUT US</h2>
<div class="abs about-corner"></div>
<div class="abs about-photo" role="img" aria-label="Friends toasting with red wine at a restaurant table"></div>
<div class="abs about-badge"><span></span></div>
<div class="abs about-rule"></div>
<h3 class="abs about-heading">Who We Are ?</h3>
<div class="abs about-copy">
  <p>Lorem Ipsum is simply dummy text of the printing and typesetting industry has been the industry's standard dummy text ever since the 1500s,</p>
  <p>when an unknown printer took a galley of type and scrambled it to make a type specimen book. It has survived not only five centuries, but also the leap into electronic typesetting, remaining essentially unchanged. It was popularised in the 1960s</p>
  <p>with the release of Letraset sheets containing Lorem Ipsum passages, and more recently with desktop publishing software...</p>
</div>
<div class="abs pill about-btn">READ MORE</div>

<section class="abs menu-section" role="img" aria-label="Dim restaurant interior backdrop"></section>
<h2 class="abs display section-title menu-title">OUR MENU</h2>
<div class="abs menu-tabs"><span>Starters</span><span class="active">Main Courses</span><span>Soups</span><span>Desserts</span></div>

<article class="dish" style="left:110px;top:1893px"><div class="dish-photo ribs" role="img" aria-label="Braised chops dish"></div><h4>BRAISED CHOPS</h4><p>Lorem Ipsum is simply dummy text of the printing text ever since the 1500s,</p><span class="price">$00.00</span></article>
<article class="dish" style="left:610px;top:1893px"><div class="dish-photo ribs" role="img" aria-label="Chicken with garlic dish"></div><h4>CHICKEN WITH GARLIC</h4><p>Lorem Ipsum is simply dummy text of the printing text ever since the 1500s,</p><span class="price">$00.00</span></article>
<article class="dish" style="left:110px;top:2048px"><div class="dish-photo fried" role="img" aria-label="Coconut fried chicken"></div><h4>COCONUT FRIED CHICKEN</h4><p>Lorem Ipsum is simply dummy text of the printing text ever since the 1500s,</p><span class="price">$00.00</span></article>
<article class="dish" style="left:610px;top:2048px"><div class="dish-photo fried" role="img" aria-label="Prime rib dish"></div><h4>PRIME RIB</h4><p>Lorem Ipsum is simply dummy text of the printing text ever since the 1500s,</p><span class="price">$00.00</span></article>
<article class="dish" style="left:110px;top:2204px"><div class="dish-photo skewer" role="img" aria-label="Chicken with garlic and tomatoes"></div><h4>CHICKEN WITH GARLIC &amp; TOMATOES</h4><p>Lorem Ipsum is simply dummy text of the printing text ever since the 1500s,</p><span class="price">$00.00</span></article>
<article class="dish" style="left:610px;top:2204px"><div class="dish-photo skewer" role="img" aria-label="Sriracha beef skewers"></div><h4>SRIRACHA BEEF SKEWERS</h4><p>Lorem Ipsum is simply dummy text of the printing text ever since the 1500s,</p><span class="price">$00.00</span></article>

<h2 class="abs display faq-title">MARLOW'S FAQ</h2>
<div class="abs faq-title-rule"></div>
<div class="faq-item open" style="top:2604px">What types of vehicles can be donated?<span class="dot"></span><p>Lorem Ipsum is simply dummy text of the printing typesetting<br>the industry's standard dummy text ever since the 1500s,</p></div>
<div class="faq-item short" style="top:2708px">Lorem Ipsum is simply&nbsp; text of the printing<span class="dot"></span></div>
<div class="faq-item short" style="top:2756px">Lorem&nbsp; simply dummy text of the?<span class="dot"></span></div>
<div class="faq-item short" style="top:2802px">Lorem Ipsum the printing and Industry<span class="dot"></span></div>
<div class="faq-item short" style="top:2848px">Lorem Ipsum is simply Industry. Lorem ?<span class="dot"></span></div>
<div class="faq-item short" style="top:2894px">Lorem&nbsp; and typesetting Industry ?<span class="dot"></span></div>
<div class="faq-item short" style="top:2940px">Lorem&nbsp; and typesetting Industry ?<span class="dot"></span></div>

<section class="abs hours" role="img" aria-label="Reserve a table and opening hours panel over a warm restaurant backdrop">
  <div class="hours-frame"></div>
  <div class="hours-kicker">RESERVE A TABLE</div>
  <div class="display hours-title">OPENING HOURS</div>
  <div class="hours-row" style="top:152px"><svg width="18" height="18" viewBox="0 0 18 18" fill="none" stroke="#222" stroke-width="1.4"><circle cx="9" cy="9" r="7.5"/><path d="M9 4v5l3 2"/></svg>Mon-Fri...... 9:00 AM-1PM</div>
  <div class="hours-row" style="top:184px"><svg width="18" height="18" viewBox="0 0 18 18" fill="none" stroke="#222" stroke-width="1.4"><circle cx="9" cy="9" r="7.5"/><path d="M9 4v5l3 2"/></svg>Sat-Sun...... 11:00 AM-1PM</div>
  <div class="hours-btn">BOOK NOW</div>
  <div class="contact-chip" style="left:57px"><span class="circle"><svg width="20" height="20" viewBox="0 0 20 20"><path d="M4 2l4 1 1 4-2 2a11 11 0 0 0 4 4l2-2 4 1 1 4-3 2C8 18 2 12 2 5z" fill="#fff"/></svg></span><div><b>CALL US</b><span class="t">+1 510 555 0142</span></div></div>
  <div class="contact-chip" style="left:231px"><span class="circle"><svg width="22" height="16" viewBox="0 0 22 16" fill="none" stroke="#fff" stroke-width="1.8"><rect x="1" y="1" width="20" height="14"/><path d="M1 1l10 8 10-8"/></svg></span><div><b>EMAIL US</b><span class="t">info@marlows.com</span></div></div>
</section>

<h2 class="abs display section-title follow-title">FOLLOW US ON</h2>
<div class="abs follow-sub">INSTAGRAM@MARLOW'S</div>
<div class="insta" style="left:77px;background:linear-gradient(135deg,#d9c7b8,#8a6a58 55%,#3b3a3a)" role="img" aria-label="Guests at a table with a phone"></div>
<div class="insta" style="left:290px;background:linear-gradient(160deg,#f0eee9,#c27a2e 55%,#7a3d14)" role="img" aria-label="Whisky being poured into a glass"></div>
<div class="insta" style="left:503px;background:linear-gradient(160deg,#2a2420,#1a1613 60%,#3a2f26)" role="img" aria-label="Dark moody bar interior"></div>
<div class="insta" style="left:715px;background:linear-gradient(135deg,#c7b49a,#e8e2d8 45%,#8a6e52)" role="img" aria-label="Hands photographing food with a phone"></div>
<div class="insta" style="left:928px;background:linear-gradient(160deg,#1e1a18,#4a3326 55%,#2a1f18)" role="img" aria-label="Wine glasses on a candle-lit table"></div>

<footer class="abs site-footer">
  <div class="abs footer-brand">MARLOW'S</div>
  <div class="footer-col" style="left:375px">
    <h5>QUICK LINKS</h5>
    <ul><li class="active">Home</li><li>About us</li><li>Menu</li><li>FAQs</li><li>Contact us</li></ul>
  </div>
  <div class="footer-col" style="left:587px">
    <h5>CONTACT INFO</h5>
    <div style="margin-top:26px">
      <div class="contact-line"><svg width="12" height="14" viewBox="0 0 20 20"><path d="M4 2l4 1 1 4-2 2a11 11 0 0 0 4 4l2-2 4 1 1 4-3 2C8 18 2 12 2 5z" fill="#ffc214"/></svg>+1 510 555 0187</div>
      <div class="contact-line"><svg width="12" height="14" viewBox="0 0 22 16"><rect x="1" y="1" width="20" height="14" fill="#ffc214"/></svg>info@marlows.com</div>
      <div class="contact-line" style="margin-top:22px"><svg width="12" height="16" viewBox="0 0 12 16"><path d="M6 0a6 6 0 0 1 6 6c0 4-6 10-6 10S0 10 0 6a6 6 0 0 1 6-6z" fill="#ffc214"/><circle cx="6" cy="6" r="2" fill="#007a68"/></svg><span>418 Harbor Lane<br>Oakland, CA 94607</span></div>
    </div>
  </div>
  <div class="footer-col newsletter" style="left:861px">
    <h5>NEWSLETTER</h5>
    <p>Lorem Ipsum is simply dummy text of the print and typesetting industry</p>
    <div class="news-input">Email Address</div>
    <div class="pill news-btn">SUBSCRIBED NOW</div>
  </div>
</footer>

<div class="abs copyright">Copyright © 2021 <b>MARLOW'S</b>, All Rights Reserved.</div>
<div class="abs socials" aria-label="Social links"><span></span><span></span><span></span><span></span></div>

</body>
</html>
```